Digital Album Cover - Piano music for wedding ceremonies and receptions

I need cover art for a piano album project that will be distributed to TuneVault, Wavelane etc. Covert art required for front of album. At this stage physical CDs will not be printed nor required it is just a digital release.
Artist name: Toby Hargrove
Album Title: Gentle Keys Melodies Wedding Ceremonies and Receptions
Volume 3
Sample piano songs are on my tunecast page
https://tunecast.example/tobyhargrovekeys/sets/gentle-keys-melodies-vol-3
Previous album artwork used from sketch hive competitions winners
https://musicvault.example/au/artist/toby-hargrove/4830917265
Target Market(s)
brides to be
grooms to be
people interested in weddings
people enjoy love songs or easy listening music
Industry/Entity Type
Wedding
Look and feel
Each slider illustrates characteristics of the customer's brand and the style your logo design should communicate.

```html
<!DOCTYPE html>
<html lang="en">
<head>
<meta charset="utf-8">
<title>Toby Hargrove – Gentle Keys Melodies, Volume 3</title>
<link rel="stylesheet" href="https://fonts.googleapis.com/css2?family=Cinzel:wght@400&family=Josefin+Sans:wght@300;400&display=swap">
<style>
  :root {
    --stage: #1c1c1c;
    --gold: #f2d21a;
    --badge: #f5e10c;
    --ink: #111111;
    --white: #ffffff;
    --photo-light: #efe7dc;
    --photo-rose: #d9a3a8;
    --photo-suit: #4a3f36;
    --photo-dark: #0d0b09;
    --keys-gold: #b89a4c;
  }
  * { margin: 0; padding: 0; box-sizing: border-box; }
  html, body {
    width: 1200px;
    height: 800px;
    overflow: hidden;
    background: var(--stage);
  }
  .canvas {
    position: relative;
    width: 1200px;
    height: 800px;
    display: flex;
    align-items: center;
    justify-content: center;
  }
  .album-cover {
    position: relative;
    width: 640px;
    height: 640px;
    overflow: hidden;
    background: var(--photo-dark);
  }
  .cover-photo {
    position: absolute;
    inset: 0;
    background:
      radial-gradient(ellipse 28% 22% at 70% 14%, var(--photo-rose) 0%, rgba(217,163,168,0) 100%),
      linear-gradient(115deg, rgba(0,0,0,0) 50%, rgba(184,154,76,0.85) 72%, var(--keys-gold) 100%),
      linear-gradient(180deg, rgba(0,0,0,0) 38%, rgba(13,11,9,0.7) 62%, var(--photo-dark) 100%),
      linear-gradient(90deg, var(--photo-suit) 0%, #6b5a4a 40%, var(--photo-light) 58%, var(--photo-light) 100%);
  }
  .rule {
    position: absolute;
    height: 2px;
    background: var(--gold);
  }
  .rule--upper { top: 268px; left: 180px; right: 0; }
  .rule--lower { top: 352px; left: 110px; right: 0; }
  .artist-name {
    position: absolute;
    top: 288px;
    left: 140px;
    font-family: "Cinzel", serif;
    font-weight: 400;
    font-size: 46px;
    letter-spacing: 0.2em;
    color: var(--gold);
    white-space: nowrap;
  }
  .album-title {
    position: absolute;
    top: 376px;
    left: 150px;
    font-family: "Josefin Sans", sans-serif;
    font-weight: 300;
    font-size: 34px;
    letter-spacing: 0.08em;
    color: var(--white);
    text-transform: uppercase;
    white-space: nowrap;
  }
  .album-subtitle {
    position: absolute;
    top: 418px;
    left: 178px;
    font-family: "Josefin Sans", sans-serif;
    font-weight: 300;
    font-size: 21px;
    letter-spacing: 0.04em;
    color: var(--white);
    white-space: nowrap;
  }
  .volume-badge {
    position: absolute;
    top: 460px;
    left: 300px;
    padding: 7px 14px 4px;
    background: var(--badge);
    font-family: "Josefin Sans", sans-serif;
    font-weight: 400;
    font-size: 19px;
    color: var(--ink);
  }
</style>
</head>
<body>
  <main class="canvas">
    <section class="album-cover">
      <div class="cover-photo" role="img" aria-label="Photograph of a groom in a suit arm in arm with a bride holding a pink and cream rose bouquet, fading into grand piano keys"></div>
      <div class="rule rule--upper"></div>
      <h1 class="artist-name">Toby Hargrove</h1>
      <div class="rule rule--lower"></div>
      <h2 class="album-title">Gentle Keys Melodies</h2>
      <p class="album-subtitle">Wedding ceremonies and receptions</p>
      <span class="volume-badge">Volume 3</span>
    </section>
  </main>
</body>
</html>
```